Flyer-Design für Heizungsbau
Zielgruppe
Wir sind ein junges, kompetentes und zertifiziertes Fachbetrieb und bieten Beratung, Fachplanung und fachmännische Installation von Wärmepumpen, Klimaanlagen und Lüftungsanlagen. Unsere Zielgruppe sind Eigentümer von Bestandsgebäuden oder Neubauten (hauptsächlich Privatkunden in mittlerem oder höherem Alter), welche eine Heizungssanierung für Heizkostenreduzierung oder neue Heizinstallation (Wärmepumpen), und/oder mehr Komfort bzw. Luftqualität in ihren Zuhause wünschen (Klima und Lüftung).
Aufgabenstellung
Schwerpunkte: 1. Ersparnis an Heizkosten, 2. Wohlgefühl und 3. Klimaschutz

```html
<!DOCTYPE html>
<html lang="de">
<head>
<meta charset="utf-8">
<title>Luftwerk – Flyer Wickelfalz</title>
<link href="https://fonts.googleapis.com/css2?family=Exo+2:wght@400;500;600&family=Roboto+Condensed:wght@300;400&display=swap" rel="stylesheet">
<style>
:root{
  --blue-dark:#16609f;
  --blue:#2f93d1;
  --blue-pale:#e2f0fa;
  --orange:#efae2e;
  --text:#4a4f55;
  --label:#222;
  --white:#fff;
}
*{box-sizing:border-box;margin:0;padding:0}
html,body{width:1080px;height:1200px;overflow:hidden;background:var(--white)}
.canvas{position:relative;width:1080px;height:1200px;overflow:hidden;font-family:"Roboto Condensed",sans-serif;color:var(--text)}
.label{position:absolute;font-family:"Roboto Condensed",sans-serif;font-size:9px;color:var(--label)}
.sheet{position:absolute;height:495px;background:var(--white);box-shadow:3px 4px 6px rgba(0,0,0,.35);overflow:hidden}
.panel-w{width:234px}
.photo{position:absolute}
.band{position:absolute;left:0;right:0;bottom:0;background:var(--blue-pale)}
.wave{position:absolute;left:0;width:100%}
.abs{position:absolute}
.brand{font-family:"Exo 2",sans-serif;font-weight:400;color:var(--blue);display:flex;align-items:center;gap:8px;white-space:nowrap}
.brand-dot{border-radius:50%;background:var(--blue)}
.brand-claim{font-family:"Roboto Condensed",sans-serif;font-size:8.6px;line-height:11px;color:var(--blue-dark)}
.web{font-family:"Exo 2",sans-serif;font-weight:600;font-size:11.5px;letter-spacing:.4px;color:var(--blue-dark);text-align:center;width:100%}
.headline{font-family:"Exo 2",sans-serif;font-size:15.5px;line-height:20px;font-weight:400}
.body{font-size:8.4px;line-height:11px;font-weight:300;color:var(--text)}
.phone{font-family:"Exo 2",sans-serif;font-weight:600;font-size:12px;letter-spacing:1px;color:var(--blue-dark);display:flex;align-items:center;gap:7px}
.feature{display:flex;gap:7px}
.feature-title{font-family:"Exo 2",sans-serif;font-size:10px;color:var(--blue-dark)}
.feature-text{font-size:7px;line-height:9px;font-weight:300;color:var(--text)}
.service{display:flex;gap:8px;margin-bottom:9px}
.service-title{font-family:"Exo 2",sans-serif;font-size:10px;color:var(--blue)}
.service-text{font-size:7px;line-height:9.5px;font-weight:300}
.orange-box{background:var(--orange);color:var(--white)}
</style>
</head>
<body>
<main class="canvas">

  <p class="label" style="left:46px;top:20px">Flyer A4 Wickelfalz auf DIN lang Einklapper nach innen</p>

  <!-- ROW 1 labels -->
  <p class="label" style="left:46px;top:48px">Titel</p>
  <p class="label" style="left:317px;top:48px">Einklapper</p>
  <p class="label" style="left:557px;top:48px">Rückseite</p>
  <p class="label" style="left:857px;top:48px">Titel</p>

  <!-- Title panel single -->
  <section class="sheet panel-w" style="left:46px;top:63px">
    <div class="abs" style="left:22px;top:78px">
      <div class="brand" style="font-size:27px"><span class="brand-dot" style="width:14px;height:14px"></span>Luftwerk</div>
      <p class="brand-claim" style="margin:12px 0 0 22px;width:160px">Beratung, Planung und fachmännische Installation von Wärmepumpen, Klimaanlagen und Lüftungsanlagen</p>
    </div>
    <div class="photo" role="img" aria-label="Frau entspannt im Sessel im hellen Wohnzimmer mit Klimagerät an der Wand" style="left:0;top:199px;width:234px;height:200px;background:linear-gradient(160deg,#e8e3dc,#cfc7bc 55%,#a9a49b)"></div>
    <div class="band" style="height:110px"></div>
    <svg class="wave" style="top:365px" height="30" viewBox="0 0 234 30" preserveAspectRatio="none"><path d="M0 22 C40 8 80 6 120 16 S200 28 234 10 L234 30 L0 30Z" fill="var(--blue-pale)"/></svg>
    <p class="web abs" style="top:452px">www.luftwerk-beispiel.de</p>
  </section>

  <!-- Outer spread -->
  <section class="sheet" style="left:317px;top:63px;width:702px">
    <!-- Einklapper -->
    <div class="abs" style="left:20px;top:24px;width:200px">
      <h2 class="headline" style="color:var(--blue-dark)">Ihr Fachbetrieb für</h2>
      <h2 class="headline" style="color:var(--blue)">Klimaanlagen und Installation</h2>
      <p class="body" style="margin-top:9px">Luftwerk GmbH ist Ihr zuverlässiger Partner im Bereich Klima-, Kälte- und Lüftungstechnik.</p>
      <p class="body" style="margin-top:9px">Als zertifiziertes Fachunternehmen bieten wir Ihnen schlüsselfertige Kälte-, Klima- und Lüftungsanlagen von marktführenden Herstellern.</p>
      <p class="body" style="margin-top:9px">Von Installations- und Instandhaltungsleistungen bis zu Hygieneinspektionen nach VDI 6022 steht unser zertifiziertes Fachpersonal Ihnen gerne zur Seite.</p>
    </div>
    <div class="photo" role="img" aria-label="Frau stellt ein Wandthermostat ein" style="left:0;top:199px;width:234px;height:200px;background:linear-gradient(150deg,#d9d4cc,#b9b2a7 50%,#8f8a84)"></div>
    <!-- Rückseite -->
    <div class="photo" role="img" aria-label="Tablet mit Energieeffizienz-Anzeige auf einem Tisch" style="left:234px;top:0;width:234px;height:199px;background:linear-gradient(160deg,#f1efec,#d8d5cf 60%,#7d8a7a)"></div>
    <!-- Title -->
    <div class="abs" style="left:490px;top:78px">
      <div class="brand" style="font-size:27px"><span class="brand-dot" style="width:14px;height:14px"></span>Luftwerk</div>
      <p class="brand-claim" style="margin:12px 0 0 22px;width:160px">Beratung, Planung und fachmännische Installation von Wärmepumpen, Klimaanlagen und Lüftungsanlagen</p>
    </div>
    <div class="photo" role="img" aria-label="Frau entspannt im Sessel im hellen Wohnzimmer mit Klimagerät an der Wand" style="left:468px;top:199px;width:234px;height:200px;background:linear-gradient(160deg,#e8e3dc,#cfc7bc 55%,#a9a49b)"></div>

    <div class="band" style="height:110px"></div>
    <svg class="wave" style="top:365px" height="34" viewBox="0 0 702 34" preserveAspectRatio="none"><path d="M0 26 C60 12 120 8 180 18 S270 30 300 20 C330 8 360 4 400 6 L480 14 C520 4 560 6 600 18 S680 26 702 12 L702 34 L0 34Z" fill="var(--blue-pale)"/></svg>
    <div class="abs" style="left:234px;top:199px;width:234px;height:200px;background:var(--white);clip-path:polygon(0 0,100% 0,100% 92%,60% 100%,0 94%)"></div>

    <div class="abs" style="left:261px;top:219px;width:190px">
      <p class="body">Gerne beantworten wir Ihnen jede Frage und helfen Ihnen mit Ihren Herausforderungen im Bereich der Klima- und Kältetechnik.</p>
      <div class="brand" style="font-size:15px;margin:38px 0 0 20px"><span class="brand-dot" style="width:9px;height:9px"></span>Luftwerk</div>
      <p class="body" style="margin:3px 0 0 37px">Luftwerk GmbH<br>Lindenallee 12<br>54321 Talheim<br>Deutschland</p>
      <p class="body" style="margin:11px 0 0 37px">E-Mail: info@luftwerk-beispiel.de<br>www.luftwerk-beispiel.de</p>
    </div>

    <div class="feature abs" style="left:37px;top:432px">
      <svg width="15" height="15" viewBox="0 0 16 16"><circle cx="8" cy="8" r="6.8" fill="none" stroke="var(--blue-dark)" stroke-width="1.5"/><path d="M4.8 8.2l2.2 2.2 4.2-4.4" fill="none" stroke="var(--blue-dark)" stroke-width="1.5"/></svg>
      <div><p class="feature-title">Höchste Qualität</p><p class="feature-text">Wir führen jede Arbeit mit höchster<br>Sorgfalt und Qualität durch</p></div>
    </div>
    <div class="phone abs" style="left:296px;top:449px">
      <svg width="12" height="12" viewBox="0 0 24 24"><path d="M6.6 10.8a15.1 15.1 0 006.6 6.6l2.2-2.2a1 1 0 011-.25 11.4 11.4 0 003.6.57 1 1 0 011 1V20a1 1 0 01-1 1A17 17 0 013 4a1 1 0 011-1h3.5a1 1 0 011 1c0 1.25.2 2.45.57 3.57a1 1 0 01-.25 1z" fill="var(--blue-dark)"/></svg>
      01234 / 567890
    </div>
    <p class="web abs" style="left:468px;width:234px;top:452px">www.luftwerk-beispiel.de</p>
  </section>

  <!-- ROW 2 labels -->
  <p class="label" style="left:46px;top:608px">Innenseite 1</p>
  <p class="label" style="left:286px;top:608px">Innenseite 2</p>
  <p class="label" style="left:586px;top:608px">Einklapper innen</p>
  <p class="label" style="left:797px;top:608px">Rückseite</p>

  <!-- Inner spread -->
  <section class="sheet" style="left:46px;top:626px;width:702px">
    <div class="orange-box abs" style="left:0;top:0;width:234px;height:199px;padding:18px 16px 0 28px">
      <h2 class="headline" style="font-size:15px;line-height:20px">Ihr Fachbetrieb für<br>umweltfreundliche,<br>effiziente und sparsame</h2>
      <h2 class="headline" style="font-size:15px;line-height:20px;color:var(--blue-dark)">Heizungslösungen</h2>
      <p class="body" style="color:var(--white);margin-top:8px;font-size:8.2px;line-height:11px">Neben dem Bereich Klima-, Kälte- und Lüftungstechnik bieten wir auch Sanierungen zur Heizkostenreduzierung oder neue Heizinstallationen, wie z.B. Wärmepumpen, und/oder Lösungen für mehr Komfort und Verbesserung der Luftqualität in ihrem Zuhause (Klima und Lüftung).</p>
    </div>
    <div class="photo" role="img" aria-label="Heizkörper in Form eines Sparschweins an heller Wand" style="left:234px;top:0;width:234px;height:199px;background:linear-gradient(160deg,#f3f2f0,#e2e0dc 60%,#d6c9b8)"></div>
    <div class="abs" style="left:468px;top:0;width:234px;height:199px;padding:18px 16px 0 26px">
      <h3 class="headline" style="font-size:12.5px;color:var(--blue);margin-bottom:9px">Unsere Leistungen</h3>
      <div class="service">
        <svg width="18" height="18" viewBox="0 0 20 20"><circle cx="10" cy="10" r="10" fill="var(--blue)"/><ellipse cx="10" cy="9" rx="5" ry="3.5" fill="#fff"/></svg>
        <div><p class="service-title">Beratung</p><p class="service-text">Wir beraten Sie vor Ort und machen auf Ihre Bedürfnisse zugeschnittene Angebote.</p></div>
      </div>
      <div class="service">
        <svg width="18" height="18" viewBox="0 0 20 20"><circle cx="10" cy="10" r="10" fill="var(--blue)"/><path d="M5 6h2l1.5 5h5l1.3-4H8" fill="none" stroke="#fff" stroke-width="1.4"/><circle cx="9" cy="13.5" r="1" fill="#fff"/><circle cx="13" cy="13.5" r="1" fill="#fff"/></svg>
        <div><p class="service-title">Verkauf</p><p class="service-text">Bei uns erhalten Sie Ihr Klimagerät zu einem günstigen Preis. Wir verkaufen nur hochwertige Anlagen.</p></div>
      </div>
      <div class="service">
        <svg width="18" height="18" viewBox="0 0 20 20"><circle cx="10" cy="10" r="10" fill="var(--blue)"/><rect x="5" y="8" width="10" height="6" fill="#fff"/><rect x="8" y="6" width="4" height="2" fill="none" stroke="#fff"/></svg>
        <div><p class="service-title">Installation</p><p class="service-text">Wir installieren Ihre Klima- oder Heizungsanlage fachmännisch und mit höchster Präzision.</p></div>
      </div>
      <div class="service">
        <svg width="18" height="18" viewBox="0 0 20 20"><circle cx="10" cy="10" r="10" fill="var(--blue)"/><path d="M6 14l5-5" stroke="#fff" stroke-width="2"/><circle cx="12.5" cy="7.5" r="2.2" fill="none" stroke="#fff" stroke-width="1.4"/></svg>
        <div><p class="service-title">Wartung</p><p class="service-text">Die notwendigen Wartungen an Ihrer Klima- oder Heizungsanlage führen wir professionell durch.</p></div>
      </div>
    </div>
    <div class="photo" role="img" aria-label="Füße in orangen Socken vor einem Sofa" style="left:0;top:199px;width:234px;height:200px;background:linear-gradient(150deg,#cfc6b9,#b8a48a 50%,#d49a4a)"></div>
    <div class="photo" role="img" aria-label="Wärmepumpe mit Innen- und Außengerät vor grauer Wand" style="left:234px;top:199px;width:234px;height:200px;background:linear-gradient(160deg,#8e8f90,#6f7071 55%,#bdbdbd)"></div>
    <div class="photo" role="img" aria-label="Paar entspannt auf dem Sofa unter einem Klimagerät" style="left:468px;top:199px;width:234px;height:200px;background:linear-gradient(160deg,#eeebe6,#d0c8bc 55%,#9a9590)"></div>
    <div class="band" style="height:112px"></div>
    <svg class="wave" style="top:360px" height="36" viewBox="0 0 702 36" preserveAspectRatio="none"><path d="M0 28 C70 14 140 10 200 22 S300 34 360 18 C420 4 480 6 540 18 S650 30 702 12 L702 36 L0 36Z" fill="var(--blue-pale)"/></svg>

    <h3 class="abs" style="left:18px;top:412px;font-family:'Exo 2',sans-serif;font-weight:600;font-size:12px;color:var(--blue-dark)">Unser Versprechen</h3>
    <div class="feature abs" style="left:36px;top:437px">
      <svg width="15" height="15" viewBox="0 0 16 16"><circle cx="8" cy="8" r="6.8" fill="none" stroke="var(--blue-dark)" stroke-width="1.5"/><path d="M8 4v4.3l2.6 1.6" fill="none" stroke="var(--blue-dark)" stroke-width="1.5"/></svg>
      <div><p class="feature-title">Schnelle Installation</p><p class="feature-text">Garantierte Installation Ihrer Klimaanlage<br>innerhalb von wenigen Wochen</p></div>
    </div>
    <div class="feature abs" style="left:283px;top:437px">
      <svg width="16" height="12" viewBox="0 0 16 12"><rect x="0.5" y="1.5" width="15" height="9" fill="var(--blue-dark)"/><circle cx="8" cy="6" r="2.3" fill="#fff"/></svg>
      <div><p class="feature-title">Faire Preise</p><p class="feature-text">Wir sind von fairen Preisen überzeugt und<br>bieten ein faires Preis-/Leistungsverhältnis</p></div>
    </div>
    <div class="feature abs" style="left:500px;top:437px">
      <svg width="16" height="12" viewBox="0 0 16 12"><rect x="0.7" y="0.7" width="14.6" height="10.6" fill="none" stroke="var(--blue-dark)" stroke-width="1.4"/><rect x="0.7" y="3" width="14.6" height="2" fill="var(--blue-dark)"/></svg>
      <div><p class="feature-title">Festpreis</p><p class="feature-text">Alle unsere Angebote sind zum Festpreis und<br>ändern sich durch mehr Aufwand auch nicht</p></div>
    </div>
  </section>

  <!-- Rückseite single -->
  <section class="sheet panel-w" style="left:797px;top:626px">
    <div class="photo" role="img" aria-label="Tablet mit Energieeffizienz-Anzeige auf einem Tisch" style="left:0;top:0;width:234px;height:199px;background:linear-gradient(160deg,#f1efec,#d8d5cf 60%,#7d8a7a)"></div>
    <div class="band" style="height:130px"></div>
    <svg class="wave" style="top:348px" height="20" viewBox="0 0 234 20" preserveAspectRatio="none"><path d="M0 8 C60 0 120 20 234 6 L234 20 L0 20Z" fill="var(--blue-pale)"/></svg>
    <div class="abs" style="left:29px;top:219px;width:190px">
      <p class="body">Gerne beantworten wir Ihnen jede Frage und helfen Ihnen mit Ihren Herausforderungen im Bereich der Klima- und Kältetechnik.</p>
      <div class="brand" style="font-size:15px;margin:38px 0 0 20px"><span class="brand-dot" style="width:9px;height:9px"></span>Luftwerk</div>
      <p class="body" style="margin:3px 0 0 37px">Luftwerk GmbH<br>Lindenallee 12<br>54321 Talheim<br>Deutschland</p>
      <p class="body" style="margin:11px 0 0 37px">E-Mail: info@luftwerk-beispiel.de<br>www.luftwerk-beispiel.de</p>
    </div>
    <div class="phone abs" style="left:64px;top:449px">
      <svg width="12" height="12" viewBox="0 0 24 24"><path d="M6.6 10.8a15.1 15.1 0 006.6 6.6l2.2-2.2a1 1 0 011-.25 11.4 11.4 0 003.6.57 1 1 0 011 1V20a1 1 0 01-1 1A17 17 0 013 4a1 1 0 011-1h3.5a1 1 0 011 1c0 1.25.2 2.45.57 3.57a1 1 0 01-.25 1z" fill="var(--blue-dark)"/></svg>
      01234 / 567890
    </div>
  </section>

</main>
</body>
</html>
```